tarang dine in

we are thai, malaysian, vietnamese restaurant. Southeast Asia, we love antique, classic, cozy ambiance, and illustrate arts form.
I would like to design lunch,dinner and limited take out menu a classic, elegant, and fun menu, healthy earthy, feels like in southeast asia

attachment are some example files that you can review it
this is us www.lovetarang-example.com
would like to follow http://www.goldenlotusrowhome-example.com 's style

restaurants that around the coner,
www.zelbaroni-example.com
http://www.frondavel-example.com
http://www.lolahartleys-example.com
http://www.harborgrillkeystone-example.com

Target Market(s)

neighbourhood, BWC students, modern and hip

Other font styles liked:
• fonts that match my old menu

Colors
faa54b
fece3e
ebf1f7
acd037
ec2027
000000

Requirements
Nice to have
• insider tips: Don't waste money on lousy food = instant regret
• Keep Calm Curry On

```html
<!DOCTYPE html>
<html lang="en">
<head>
<meta charset="utf-8">
<title>tarang – Southeast Asian Street Food Menu</title>
<link rel="stylesheet" href="https://fonts.googleapis.com/css2?family=Arimo:wght@400;700&family=Fjalla+One&family=Cabin:wght@400&family=Dancing+Script:wght@600&display=swap">
<style>
  :root{
    --wood-light:#ebe8e2;
    --wood-mid:#dcd8d0;
    --ink:#1f1f1f;
    --brown:#6b4526;
    --dot-green:#acd037;
    --band-green:#8cc63f;
    --band-yellow:#f2c23a;
    --flower:#fece3e;
    --leaf:#9bbf3a;
    --accent-orange:#faa54b;
  }
  *{margin:0;padding:0;box-sizing:border-box}
  html,body{width:849px;height:1200px;overflow:hidden}
  body{background:#fff}
  .menu{
    position:relative;width:849px;height:1200px;overflow:hidden;
    background:
      repeating-linear-gradient(90deg, rgba(0,0,0,0) 0 84px, rgba(120,110,95,.10) 84px 86px),
      linear-gradient(180deg,var(--wood-light),var(--wood-mid));
    font-family:'Arimo',Arial,sans-serif;color:var(--ink);
  }
  .band-left{position:absolute;left:0;top:0;width:28px;height:1200px;background:linear-gradient(90deg,#7db52f,var(--band-green))}
  .band-right{position:absolute;right:0;top:0;width:24px;height:1200px;background:linear-gradient(90deg,var(--band-yellow),#e8b12c)}
  .flower{position:absolute;left:81px;top:64px;width:48px;height:48px;border-radius:50%;background:var(--flower)}
  .splash{position:absolute;border-radius:50%}
  .splash-left{left:356px;top:96px;width:26px;height:16px;background:var(--flower)}
  .splash-right{left:772px;top:116px;width:30px;height:16px;background:var(--accent-orange)}
  .brand{position:absolute;left:386px;top:18px;width:380px;text-align:center}
  .brand-name{font-family:'Fjalla One',sans-serif;font-size:96px;line-height:1.1;color:var(--ink);letter-spacing:1px}
  .brand-tagline{position:absolute;left:416px;top:118px}
  .tagline-text{font-family:'Fjalla One',sans-serif;font-size:15px;fill:var(--ink);letter-spacing:1px}
  .motto{position:absolute;left:82px;top:155px;font-family:'Dancing Script',cursive;font-size:20px;color:var(--ink)}
  .heading{position:absolute;font-family:'Fjalla One',sans-serif;font-size:23px;color:var(--brown);line-height:28px;white-space:nowrap}
  .heading .note{font-family:'Dancing Script',cursive;font-size:20px;color:var(--ink);margin-left:10px}
  .dots{position:absolute;height:0;border-top:4px dotted var(--dot-green)}
  .item{position:absolute;font-size:15.5px;line-height:17px}
  .item .name{display:block}
  .item .price{position:absolute;top:0}
  .item .desc{display:block;font-family:'Cabin',sans-serif;font-size:10px;line-height:17px;margin-top:3px}
  .col-left .item{left:81px;width:305px}
  .col-left .item .price{left:280px}
  .col-left .item .name,.col-left .item .desc{width:270px}
  .col-right .item{left:472px;width:300px}
  .col-right .item .price{right:0}
  .col-right .item .name,.col-right .item .desc{width:255px}
  .beer{position:absolute;font-size:15.5px;line-height:17px}
  .leaf{position:absolute;left:402px;top:1080px;width:44px;height:44px;border-radius:50% 0 50% 0;background:var(--leaf)}
  .leaf-corner{position:absolute;left:28px;top:1096px;width:36px;height:24px;border-radius:50% 0 50% 0;background:var(--leaf)}
  .signoff{position:absolute;left:340px;top:1126px;width:170px;text-align:center;font-family:'Dancing Script',cursive;font-size:20px;color:var(--ink)}
</style>
</head>
<body>
<main class="menu">
  <div class="band-left"></div>
  <div class="band-right"></div>
  <div class="flower" role="img" aria-label="Yellow frangipani flower ornament"></div>
  <div class="splash splash-left" role="img" aria-label="Yellow splash ornament"></div>
  <div class="splash splash-right" role="img" aria-label="Orange splash ornament"></div>

  <header>
    <div class="brand"><span class="brand-name">tarang</span></div>
    <svg class="brand-tagline" width="330" height="60" viewBox="0 0 330 60" aria-label="Southeast Asian Street Food">
      <defs><path id="tagline-arc" d="M5,40 Q165,0 325,48"/></defs>
      <text class="tagline-text"><textPath href="#tagline-arc">SOUTHEAST ASIAN STREET FOOD</textPath></text>
    </svg>
    <p class="motto">Where spice is our vine</p>
  </header>

  <!-- Specialty -->
  <div class="dots" style="left:78px;top:202px;width:160px"></div>
  <h2 class="heading" style="left:247px;top:190px">SPECIALTY</h2>
  <div class="dots" style="left:374px;top:202px;width:433px"></div>

  <section class="col-left">
    <div class="item" style="top:232px"><span class="name">Rendang Nasi Lemak<br>Classic Bowl</span><span class="price">€10</span><span class="desc">Coconut-pandanus jasmine rice, rendang curry, hard boiled egg, sambal chili, Pineapple achat, cucumbers and roasted peanuts.</span></div>
    <div class="item" style="top:335px"><span class="name">Banh Mi Saigon</span><span class="price">€10</span><span class="desc">Cucumbers, pickled carrots and radishes, homemade Chinese sausage, cilantro, bologna pork pate, hot green chiles.</span></div>
    <div class="item" style="top:420px"><span class="name">Ka Prao Basil Sauce</span><span class="price">€10</span><span class="desc">Garlic, Thai chilli, bell pepper, onion, egg, fresh Thai basil leaves.</span></div>

    <div class="dots" style="left:78px;top:527px;width:62px"></div>
    <h2 class="heading" style="left:153px;top:515px">DESSERTS</h2>
    <div class="dots" style="left:265px;top:527px;width:113px"></div>

    <div class="item" style="top:557px"><span class="name">Butter Pound Cake Fried Ice<br>Cream</span><span class="price">€3</span></div>
    <div class="item" style="top:609px"><span class="name">China Town Style Coffee<br>with Cinnamon Cookies</span><span class="price">€3</span></div>
    <div class="item" style="top:660px"><span class="name">Coconut Jam &amp; Butter Toast</span><span class="price">€3</span></div>
    <div class="item" style="top:694px"><span class="name">Coconut Cream</span><span class="price">€3</span></div>
    <div class="item" style="top:729px"><span class="name">&nbsp;Mango Sticky Rice</span><span class="price">€3</span></div>
    <div class="item" style="top:763px"><span class="name">Classic Shaved Ice with Rose<br>syrup and Palm Sugar ice cream</span><span class="price">€3</span></div>

    <div class="dots" style="left:78px;top:835px;width:62px"></div>
    <h2 class="heading" style="left:149px;top:823px">BEER<span class="note">€7 for all</span></h2>
    <div class="dots" style="left:300px;top:835px;width:78px"></div>

    <div class="beer" style="left:81px;top:866px">Riverbend</div>
    <div class="beer" style="left:81px;top:900px">Harbor Lager</div>
    <div class="beer" style="left:81px;top:934px">Sunray</div>
    <div class="beer" style="left:81px;top:968px">Star Point</div>
    <div class="beer" style="left:323px;top:866px">Stripe Lager</div>
    <div class="beer" style="left:323px;top:900px">Lionpeak</div>
    <div class="beer" style="left:323px;top:934px">Northwind</div>
  </section>

  <section class="col-right">
    <div class="item" style="top:232px"><span class="name">Thai Green Curry</span><span class="price">€10</span><span class="desc">Fresh pounded Green chilli paste, lemongrass, bamboo strips, Thai eggplant, bell pepper, long beans, fresh basil</span></div>
    <div class="item" style="top:300px"><span class="name">Vegeterian Curry Clay Pot</span><span class="price" style="top:18px">€12</span><span class="desc">Cabbage, potatoes, long beans, carrots, fried tofu, tomatoes, eggplant, fresh chilli</span></div>
    <div class="item" style="top:369px"><span class="name">Cashew Smoked Chilli</span><span class="price">€10</span><span class="desc">Bell pepper, cashew nuts, onion, Thai sweet chilli paste</span></div>

    <div class="dots" style="left:472px;top:442px;width:98px"></div>
    <h2 class="heading" style="left:584px;top:430px">SIDE ORDER</h2>
    <div class="dots" style="left:713px;top:442px;width:98px"></div>

    <div class="item" style="top:472px"><span class="name">Thai Jasmine Rice</span><span class="price">€1</span></div>
    <div class="item" style="top:506px"><span class="name">Coconut Flavored Rice</span><span class="price">€2</span></div>
    <div class="item" style="top:540px"><span class="name">Sticky Coconut Rice</span><span class="price">€3</span></div>
    <div class="item" style="top:574px;left:470px"><span class="name">Sambal Egg</span><span class="price">€3</span></div>

    <div class="dots" style="left:472px;top:630px;width:32px"></div>
    <h2 class="heading" style="left:528px;top:618px">COLD BEVERAGES</h2>
    <div class="dots" style="left:745px;top:630px;width:62px"></div>

    <div class="item" style="top:660px"><span class="name">Origina Sparkling Citrus</span><span class="price">€3</span></div>
    <div class="item" style="top:694px"><span class="name">Calamansi Honey Jasmine Tea</span><span class="price">€3</span></div>
    <div class="item" style="top:729px"><span class="name">Fresh Coconut Juice</span><span class="price">€3</span></div>
    <div class="item" style="top:763px"><span class="name">Fresh Mango Passion Fruits<br>Smoothie</span><span class="price">€3</span></div>
    <div class="item" style="top:814px"><span class="name">Thai Iced Tea</span><span class="price">€3</span></div>
    <div class="item" style="top:848px"><span class="name">Viet Ice Coffee</span><span class="price">€3</span></div>

    <div class="dots" style="left:472px;top:904px;width:55px"></div>
    <h2 class="heading" style="left:537px;top:892px">HOT BEVERAGES</h2>
    <div class="dots" style="left:722px;top:904px;width:89px"></div>

    <div class="item" style="top:934px"><span class="name">Viet Style Hot Coffee</span><span class="price">€3</span></div>
    <div class="item" style="top:968px"><span class="name">Hand Pulled Milk Tea</span><span class="price">€3</span></div>
    <div class="item" style="top:1002px"><span class="name">Oolong Tea</span><span class="price">€3</span></div>
    <div class="item" style="top:1036px"><span class="name">Green Tea</span><span class="price">€3</span></div>
  </section>

  <footer>
    <div class="leaf" role="img" aria-label="Green leaf sprig ornament"></div>
    <div class="leaf-corner" role="img" aria-label="Green leaf ornament"></div>
    <div class="dots" style="left:229px;top:1143px;width:106px"></div>
    <p class="signoff">Keep Calm Carry on</p>
    <div class="dots" style="left:512px;top:1143px;width:61px"></div>
  </footer>
</main>
</body>
</html>
```